terras letterhead

We would like to create a new letterhead that our company will use for proposals, invoices, statements and letters. Our company name is Terra-Crafters. We are a landscape design/build and landscape maintenance company. We have a web site Terra-Crafters.example where our logo (the leaf with the lettering within it only) is displayed.

Industry/Entity Type

Graphic Design

Requirements
Must have
• Address and info on our current letterhead (uploaded)
Nice to have
• We would like the design to look presentable in grey scale as well as color.
Should not have
• Do not want to infringe much on the normal useable area within the normal print areas.

```html
<!DOCTYPE html>
<html lang="en">
<head>
<meta charset="utf-8">
<title>Terra-Crafters Letterhead</title>
<link href="https://fonts.googleapis.com/css2?family=Arimo:wght@400&display=swap" rel="stylesheet">
<style>
  :root {
    --backdrop: #e6e4e0;
    --paper: #ffffff;
    --ink: #111111;
    --leaf-green: #3b4a22;
  }
  html, body {
    margin: 0;
    padding: 0;
    width: 848px;
    height: 1200px;
    overflow: hidden;
    background: var(--backdrop);
  }
  .letterhead {
    position: absolute;
    left: 64px;
    top: 91px;
    width: 720px;
    height: 1018px;
    background: var(--paper);
    box-shadow: 0 2px 10px rgba(0,0,0,0.18);
  }
  .brand {
    position: absolute;
    left: 24px;
    top: 86px;
    display: flex;
    align-items: center;
    gap: 10px;
  }
  .brand-dot {
    width: 16px;
    height: 16px;
    border-radius: 50%;
    background: var(--leaf-green);
  }
  .brand-name {
    font-family: "Arimo", Arial, sans-serif;
    font-weight: 400;
    font-size: 24px;
    color: var(--leaf-green);
  }
  .contact {
    position: absolute;
    right: 90px;
    top: 44px;
    margin: 0;
    text-align: center;
    font-style: normal;
    font-family: "Arimo", Arial, sans-serif;
    font-size: 16.5px;
    line-height: 17px;
    color: var(--ink);
    letter-spacing: -0.3px;
  }
  .contact p { margin: 0; white-space: nowrap; }
  .header-swoop {
    position: absolute;
    left: 0;
    top: 110px;
    width: 720px;
    height: 60px;
  }
</style>
</head>
<body>
  <main class="letterhead">
    <div class="brand">
      <span class="brand-dot"></span>
      <span class="brand-name">Terra-Crafters</span>
    </div>
    <address class="contact">
      <p>118 Meadowbrook Lane. Fernhill,NJ 07099</p>
      <p>(555) 010 - 1155</p>
      <p>FAX: (555) 010 - 7820</p>
      <p>service@terra-crafters.example</p>
      <p>www.terra-crafters.example</p>
    </address>
    <svg class="header-swoop" viewBox="0 0 720 60" aria-hidden="true">
      <path d="M0 55 C 200 33, 450 23, 720 23 L 720 28 C 450 28, 200 38, 0 62 Z" fill="var(--leaf-green)"/>
    </svg>
  </main>
</body>
</html>
```